Web Design Company Needs New Look

We are a very, very busy web development company that doesn't have the time to look after our own website because of the workload. Now the site has become stale and an afterthought. I need a designer that can deliver a home page template, basic inside page template and portfolio template that will be fresh, amazing looking, and show off the qualities clients love about us.
I want strong imagery that I can help choose (although your input would be greatly appreciated), amazing fonts, clean-clean-clean and really , really need to lean on a great creative designer that can take the lead on this as we have very minimal time available due to our workload.
It Company

```html
<!DOCTYPE html>
<html lang="en">
<head>
<meta charset="utf-8">
<title>brisk — Web Development Company</title>
<link rel="stylesheet" href="https://fonts.googleapis.com/css2?family=Lato:ital,wght@0,100;0,300;0,400;0,700;0,900;1,300&display=swap">
<style>
:root{
  --nav-bg:#262626;
  --accent:#e5534b;
  --white:#ffffff;
  --ink:#444444;
  --ink-soft:#666666;
  --muted:#888888;
  --band:#f6f6f6;
  --footer:#2f2f2f;
  --footer-base:#232323;
  --footer-text:#9a9a9a;
  --dot:#555555;
}
*{margin:0;padding:0;box-sizing:border-box}
html,body{width:1200px;height:2251px;overflow:hidden}
body{font-family:"Lato",Arial,sans-serif;color:var(--ink);background:var(--white);position:relative}

/* Navigation */
.site-nav{position:absolute;top:0;left:0;width:1200px;height:74px;background:var(--nav-bg)}
.brand{position:absolute;left:218px;top:17px;font-size:32px;font-weight:300;color:var(--white);letter-spacing:1px;line-height:36px}
.nav-menu{position:absolute;left:362px;top:0;width:652px;height:74px;display:flex;justify-content:space-between;align-items:center;list-style:none}
.nav-menu li{font-size:11px;font-weight:700;color:var(--white);text-transform:uppercase;letter-spacing:.3px}
.nav-menu li.is-current{color:var(--accent)}

/* Hero */
.hero{position:absolute;top:74px;left:0;width:1200px;height:601px;
  background:radial-gradient(ellipse at 30% 40%,#3c4450 0%,rgba(60,68,80,0) 45%),
             linear-gradient(180deg,#dfe3e6 0%,#b9c6cf 30%,#8aa3b4 60%,#a9c3d3 100%)}
.hero-copy{position:absolute;top:0;left:0;width:1200px;text-align:center;color:var(--white)}
.hero-title{position:absolute;top:305px;width:1200px;font-size:94px;line-height:100px;font-weight:100;letter-spacing:-1px}
.hero-title strong{font-weight:900}
.hero-sub{position:absolute;top:412px;width:1200px;font-size:32px;line-height:36px;font-weight:400}
.hero-sub em{font-weight:300}
.hero-sub b{font-weight:700}
.hero-line{position:absolute;top:446px;width:1200px;font-size:23px;line-height:28px;font-weight:300}
.hero-button{position:absolute;top:513px;left:544px;width:112px;height:35px;border:2px solid var(--white);border-radius:3px;font-size:13px;font-weight:700;line-height:31px;color:var(--white)}

/* Services */
.services{position:absolute;top:675px;left:0;width:1200px;height:330px;background:var(--band)}
.service{position:absolute;top:60px;width:190px;text-align:center}
.service--design{left:179px}
.service--hosting{left:505px}
.service--promotion{left:831px}
.service-icon{display:block;margin:0 auto;width:52px;height:52px;border-radius:8px;background:#5a5a5a}
.service-title{margin-top:22px;font-size:14px;font-weight:700;color:var(--ink)}
.service-lead{margin-top:8px;font-size:11px;color:var(--ink)}
.service-text{margin-top:14px;font-size:9.5px;line-height:11.5px;color:var(--ink-soft);text-align:justify;padding:0 5px}

/* Featured works */
.works{position:absolute;top:1005px;left:0;width:1200px;height:728px;background:var(--white)}
.section-title{width:1200px;text-align:center;font-size:24px;line-height:30px;font-weight:300;color:var(--ink);text-transform:uppercase}
.section-title strong{font-weight:700}
.works .section-title{position:absolute;top:65px}
.works-sub{position:absolute;top:104px;width:1200px;text-align:center;font-size:15px;font-weight:300;color:var(--ink-soft)}
.works-grid{position:absolute;top:150px;left:182px;width:834px;display:grid;grid-template-columns:repeat(4,203px);grid-auto-rows:165px;gap:7px}
.work-tile{display:block}
.tile-1{background:linear-gradient(135deg,#8a7d86,#c8bcc0)}
.tile-2{background:linear-gradient(135deg,#2a63a8,#8cbfe4)}
.tile-3{background:linear-gradient(135deg,#b49a86,#e0d2c6)}
.tile-4{background:linear-gradient(135deg,#3c5a9c,#6e86b8)}
.tile-5{background:linear-gradient(135deg,#d2d0cf,#9d9a98)}
.tile-6{background:linear-gradient(135deg,#c19a86,#eae0da)}
.tile-7{background:linear-gradient(135deg,#3e6d8a,#5d7f92)}
.tile-8{background:linear-gradient(135deg,#d6b9a2,#9e9590)}
.tile-9{background:linear-gradient(135deg,#8c7f95,#c6b7b5)}
.tile-10{background:linear-gradient(135deg,#7c6a6e,#b79a86)}
.tile-11{background:linear-gradient(135deg,#c9beb2,#8a7460)}
.tile-12{background:linear-gradient(135deg,#2a3a44,#7a8890)}
.pager{position:absolute;top:679px;left:571px;display:flex;gap:2px}
.pager span{width:12px;height:12px;border-radius:50%;background:var(--dot)}
.pager span.is-active{background:var(--accent)}

/* Why choose */
.why{position:absolute;top:1733px;left:0;width:1200px;height:245px;background:var(--band)}
.why .section-title{position:absolute;top:52px}
.why-lead{position:absolute;top:101px;width:1200px;text-align:center;font-size:13px;font-weight:700;color:var(--ink);text-transform:uppercase;letter-spacing:.3px}
.why-text{position:absolute;top:124px;left:182px;width:834px;font-size:14px;line-height:22.5px;font-weight:400;color:var(--ink-soft)}

/* Footer */
.site-footer{position:absolute;top:1978px;left:0;width:1200px;height:211px;background:var(--footer);text-align:center}
.footer-title{position:absolute;top:37px;width:1200px;font-size:22px;font-weight:700;color:var(--white)}
.footer-tagline{position:absolute;top:74px;width:1200px;font-size:15px;font-weight:300;color:var(--footer-text)}
.contact-line{position:absolute;top:106px;width:1200px;display:flex;justify-content:center;gap:26px;font-size:11px;color:#bdbdbd}
.contact-line span{display:flex;align-items:center;gap:8px}
.social{position:absolute;top:145px;left:533px;display:flex;gap:5px}
.social span{width:20px;height:20px;border-radius:50%}
.social .s1{background:#e8a23d}
.social .s2{background:#4a6db4}
.social .s3{background:#4ea8dd}
.social .s4{background:#e07aa8}
.social .s5{background:#d94a4a}
.footer-base{position:absolute;top:2189px;left:0;width:1200px;height:62px;background:var(--footer-base);text-align:center;font-size:10px;line-height:62px;color:#bdbdbd}
</style>
</head>
<body>

<header class="site-nav">
  <div class="brand">brisk</div>
  <ul class="nav-menu">
    <li class="is-current">Home</li>
    <li>Our Company</li>
    <li>Services</li>
    <li>Portfolio</li>
    <li>Free Resources</li>
    <li>Pay Online</li>
    <li>Contact Us</li>
  </ul>
</header>

<section class="hero" role="img" aria-label="Close-up photograph of a smartphone lying on a glossy table in soft blue light">
  <div class="hero-copy">
    <h1 class="hero-title">We are <strong>brisk</strong></h1>
    <p class="hero-sub"><em>web development</em> company based on <b>MARS</b></p>
    <p class="hero-line">and we would love to turn ideas into beautiful things.</p>
    <div class="hero-button">Learn more</div>
  </div>
</section>

<section class="services">
  <article class="service service--design">
    <span class="service-icon" role="img" aria-label="Sewing machine icon"></span>
    <h2 class="service-title">Website Design</h2>
    <p class="service-lead">Custom designs. Powerful Platforms.</p>
    <p class="service-text">Find out why more than 90% of projects are started by referrals or clients that have already worked with us before. We offer custom designs in powerful platforms that give you control to keep your website up to date.</p>
  </article>
  <article class="service service--hosting">
    <span class="service-icon" role="img" aria-label="Hand holding a browser window icon"></span>
    <h2 class="service-title">Website Hosting</h2>
    <p class="service-lead">We can host or support your site.</p>
    <p class="service-text">We can keep your website hosted, backed up daily, and even update your site for you with affordable hosting and support packages. We offer multiple plans with different levels of pricing and support.</p>
  </article>
  <article class="service service--promotion">
    <span class="service-icon" role="img" aria-label="Gramophone icon"></span>
    <h2 class="service-title">Website Promotion</h2>
    <p class="service-lead">Is your website being found?</p>
    <p class="service-text">Launching a website is only half the battle. You need traffic for website success. And the traffic should be relevant. Brisk can help you with social media marketing, search engine optimization, and PPC management.</p>
  </article>
</section>

<section class="works">
  <h2 class="section-title">Our <strong>Featured Works</strong></h2>
  <p class="works-sub">Original design solutions</p>
  <div class="works-grid">
    <div class="work-tile tile-1" role="img" aria-label="Portfolio project: textured close-up with home screen lettering"></div>
    <div class="work-tile tile-2" role="img" aria-label="Portfolio project: blue close-up with bold lettering"></div>
    <div class="work-tile tile-3" role="img" aria-label="Portfolio project: warm textured close-up with a thin arc"></div>
    <div class="work-tile tile-4" role="img" aria-label="Portfolio project: blue close-up with large light lettering"></div>
    <div class="work-tile tile-5" role="img" aria-label="Portfolio project: pale grey soft-focus photograph"></div>
    <div class="work-tile tile-6" role="img" aria-label="Portfolio project: warm blurred texture photograph"></div>
    <div class="work-tile tile-7" role="img" aria-label="Portfolio project: slate blue close-up photograph"></div>
    <div class="work-tile tile-8" role="img" aria-label="Portfolio project: warm blurred photograph with live lettering"></div>
    <div class="work-tile tile-9" role="img" aria-label="Portfolio project: soft-focus photograph with large lettering"></div>
    <div class="work-tile tile-10" role="img" aria-label="Portfolio project: textured brown close-up photograph"></div>
    <div class="work-tile tile-11" role="img" aria-label="Portfolio project: curved object edge in soft light"></div>
    <div class="work-tile tile-12" role="img" aria-label="Portfolio project: dark blue-grey soft-focus photograph"></div>
  </div>
  <div class="pager"><span class="is-active"></span><span></span><span></span><span></span></div>
</section>

<section class="why">
  <h2 class="section-title">Why <strong>Choose Brisk</strong></h2>
  <p class="why-lead">90% of our projects are started by referrals or repeat clients.</p>
  <p class="why-text">Think about that for a moment. Nearly every new project we start is by a client that was so happy with our previous work that they want to work with us again. Even our new contacts are from previous clients referring us to them. Simply put, clients love our work and recommend us time and time again.</p>
</section>

<footer class="site-footer">
  <h2 class="footer-title">Get in Touch</h2>
  <p class="footer-tagline">Fast and affordable solutions for website design, hosting and promotion on the internet.</p>
  <div class="contact-line">
    <span>
      <svg width="8" height="11" viewBox="0 0 8 11" aria-hidden="true"><path d="M4 0a4 4 0 0 1 4 4c0 3-4 7-4 7S0 7 0 4a4 4 0 0 1 4-4z" fill="#e5534b"/><circle cx="4" cy="4" r="1.5" fill="#2f2f2f"/></svg>
      220 HARBOR AVE. SUITE 140 LAKEVIEW, MI 48000
    </span>
    <span>
      <svg width="11" height="9" viewBox="0 0 11 9" aria-hidden="true"><path d="M0 3c0-2 3-3 5.5-3S11 1 11 3L9 4 7.5 2.5h-4L2 4z" fill="#e5534b"/><rect x="2" y="5" width="7" height="4" rx="1" fill="#e5534b"/></svg>
      800.555.0142
    </span>
  </div>
  <div class="social" aria-label="Social links">
    <span class="s1"></span><span class="s2"></span><span class="s3"></span><span class="s4"></span><span class="s5"></span>
  </div>
</footer>
<div class="footer-base">© 2013 Brisk. All Rights Reserved.</div>

</body>
</html>
```